Lindenhof Wissensportal - Redesign
Die Seite http://www.lindenhof-wissensportal.de soll einem kompletten neu designed werden. Der Inhalt soll so übernommen werden. Auf der Startseite soll ein Blog inegriert werden. Typische Features wie Zeitachsenarchiv, Tagclouds, letzte Kommentare und Social Media Links sollen intelligent integriert werden. Alle Menüpunkte sollen als Themenvorschläge auf der Wesite mit entsprechenden Bildern integriert werden.
Beispiel: Menüpunkt Top Emittenten. Auf der Wesite wird dann beispielsweise ein kleiner Kasten mit Headline "Wer sind die Besten?" inetgriert. Im Kasten ist ein ansprechends Bild und ein kurzer Text: "Die bseten Emittenten finden Sie hier!"
Ein intelligentes Cockpit soll den User auf jeder Seite begleiten. Hier wird der Newsletter angeboten und die Social Media Links verpackt. Darüber hinaus eine E-Mail zur Kontaktaufnahme.
Als Leitfarben sehen wir folgende Kombinationsmöglichkeiten:
a. Grau - Orange
b. Grau - Froschgrün
c. Graubraun - Orange
Bitte berücksichtigen Sie, dass unsere Besucher zwischen 40 und 70 Jahre alt sind.
Die späterr Programmierung soll in Wordpress stattfinden!
Bei weiteren Fragen wenden Sie sich gerne an mich.
Viel Erfolg!

```html
<!DOCTYPE html>
<html lang="de">
<head>
<meta charset="utf-8">
<title>Lindenhof Wissensportal</title>
<link href="https://fonts.googleapis.com/css2?family=Arvo:wght@400;700&family=Roboto:wght@300;400&display=swap" rel="stylesheet">
<style>
:root{
  --navy:#1d3a6b;
  --green:#95c11f;
  --ink:#222;
  --grey:#9a9a9a;
  --light:#b5b5b5;
  --white:#fff;
}
*{box-sizing:border-box;margin:0;padding:0}
html,body{width:841px;height:1200px;overflow:hidden;background:var(--white)}
body{position:relative;font-family:'Roboto',Arial,sans-serif;color:var(--ink)}
.abs{position:absolute}

/* navigation */
.main-nav{left:4px;top:8px;width:834px;height:45px;background:var(--navy);display:flex;align-items:center}
.main-nav a{color:var(--white);text-decoration:none;font-size:14px;letter-spacing:.2px;text-transform:uppercase;position:absolute;top:15px}
.main-nav a.is-active{left:4px;top:-4px;height:53px;width:117px;border:2px solid var(--green);background:var(--navy);display:flex;align-items:center;justify-content:center}
.main-nav a:not(.is-active)::before{content:"";display:inline-block;width:7px;height:7px;background:var(--white);clip-path:polygon(100% 0,100% 100%,0 100%);margin-right:3px;vertical-align:2px}

/* hero */
.hero{left:4px;top:61px;width:834px;height:291px;border:3px solid var(--green);border-bottom-width:8px;background:var(--white)}
.hero-photo{left:0;top:0;width:405px;height:280px;background:linear-gradient(135deg,#c9a48d 0%,#e0c2ad 40%,#f3e8e0 80%,#fff 100%)}
.hero-title{left:413px;top:176px;font-size:30px;font-weight:300;letter-spacing:-.8px;color:var(--ink)}
.hero-title em{font-style:normal;color:var(--navy)}
.hero-claim{right:14px;top:218px;font-family:'Arvo',Georgia,serif;font-weight:700;font-size:21px;color:var(--ink)}

/* section headings */
.section-head{font-family:'Arvo',Georgia,serif;font-size:18px;line-height:22px;color:var(--ink);padding-left:28px;position:absolute}
.section-head::before{content:"";position:absolute;left:0;top:3px;width:14px;height:14px;background:var(--navy);clip-path:polygon(100% 0,100% 100%,0 100%)}
.section-note{position:absolute;font-size:8.5px;line-height:11px;color:var(--light);font-weight:300}

/* topic tiles */
.tile-navy{left:200px;top:390px;width:185px;height:122px;background:var(--navy)}
.tile-green{left:200px;top:516px;width:185px;height:59px;background:var(--green);color:var(--white);padding:10px 13px}
.tile-green h3{font-size:12.5px;font-weight:400;letter-spacing:-.3px}
.tile-green p{font-size:7.5px;line-height:10px;color:#dcefb0;font-weight:300;margin-top:6px}
.tile-image{height:140px;width:187px}
.tile-image .visual{position:absolute;left:0;top:14px;width:100%;height:116px}
.tile-image .label{position:absolute;right:0;top:0;width:115px;height:17px;background:var(--navy);color:var(--white);font-size:12px;letter-spacing:-.4px;padding:1px 8px}
.tile-image .bar{position:absolute;left:0;bottom:0;width:100%;height:5px;background:var(--navy)}
.cards{background:linear-gradient(160deg,#f2f2f2,#d8d8d8 70%,#fff)}
.crown{background:linear-gradient(180deg,#fff 0%,#f1cf5a 35%,#d9a520 70%,#f5e2a0 100%)}

.dots{position:absolute;left:15px;width:810px;border-top:2px dotted #3a5588;height:0}

/* blog */
.post{position:absolute;top:628px;width:178px}
.post h2{font-size:20px;line-height:24px;font-weight:300;letter-spacing:-.3px;color:#444}
.post.is-featured h2{color:var(--green)}
.post p{margin-top:10px;font-size:11px;line-height:15px;font-weight:300;color:var(--light)}
.more{position:absolute;top:800px;font-size:12px;color:var(--green);text-decoration:underline;font-weight:300}
.more::before{content:"";display:inline-block;width:7px;height:7px;background:var(--green);clip-path:polygon(100% 0,100% 100%,0 100%);margin-right:2px}

/* cockpit */
.vline{position:absolute;top:868px;height:186px;border-left:2px dotted #3a5588;width:0}
.small{position:absolute;font-size:8.5px;line-height:11px;color:#666;font-weight:300}
.field-label{position:absolute;height:17px;background:var(--navy);color:var(--white);font-size:9.5px;text-align:center;line-height:17px}
.field{position:absolute;height:17px;border:1px solid var(--navy);font-size:9.5px;line-height:15px;padding-left:5px;color:#333}
.btn{position:absolute;height:17px;background:var(--navy);color:var(--white);font-size:9.5px;text-align:center;line-height:17px}
.contact{position:absolute;left:324px;top:932px;font-size:8.5px;line-height:11px;color:#222}
.contact p{margin-bottom:11px}

.legal{position:absolute;right:18px;top:1088px;font-size:9px;color:#222}
.site-footer{left:4px;top:1108px;width:834px;height:92px;background:var(--navy);border-top:6px solid var(--green);color:var(--white);text-align:center;font-size:13px;font-weight:300;padding-top:30px;line-height:17px}
</style>
</head>
<body>

<nav class="main-nav abs">
  <a class="is-active" href="#">Startseite</a>
  <a href="#" style="left:134px">Warum Fonts</a>
  <a href="#" style="left:280px">Sektoren</a>
  <a href="#" style="left:404px">Top Emittenten</a>
  <a href="#" style="left:563px;top:14px">Ratings</a>
  <a href="#" style="left:672px;top:14px">Kaufen ohne Agio</a>
</nav>

<header class="hero abs">
  <div class="hero-photo abs" role="img" aria-label="Porträtfoto eines lächelnden Beraters mit Brille"></div>
  <h1 class="hero-title abs">Lindenhof <em>Wissensportal</em></h1>
  <p class="hero-claim abs">... suchen lohnt sich</p>
</header>

<h2 class="section-head" style="left:22px;top:387px">Lindenhof<br>Wissensportal</h2>
<p class="section-note" style="left:45px;top:436px;width:130px">Sie wollen die besten geschlos-<br>senen Fonds finden?</p>

<div class="tile-navy abs"></div>
<div class="tile-green abs">
  <h3>Warum Fonds?</h3>
  <p>Diti tom il ils aut asperna tibus.<br>Atestore alia verum dolore solorerfero</p>
</div>

<div class="tile-image abs" style="left:403px;top:436px">
  <div class="visual cards" role="img" aria-label="Foto von aufgefächerten Spielkarten mit Assen"></div>
  <div class="label">Sektoren</div>
  <div class="bar"></div>
</div>
<div class="tile-image abs" style="left:607px;top:436px">
  <div class="visual crown" role="img" aria-label="Foto einer goldenen Krone"></div>
  <div class="label">Top Emittenten</div>
  <div class="bar"></div>
</div>

<div class="dots" style="top:607px;left:4px;width:808px"></div>

<h2 class="section-head" style="left:22px;top:630px">Blogs</h2>
<p class="section-note" style="left:50px;top:658px;width:110px">Sae pa serchic tem fugia-<br>tent ut volorem quo diat et<br>ommolup tatque venis</p>

<article class="post is-featured" style="left:196px">
  <h2>Itibus, que etus debi-<br>tios et rehent rehent<br>reptasperis audame</h2>
  <p>Os sandae nonserrum autenihita quid eserspe dipsapis eum ut rehe-ne est ea volupta simus explanimi, quaes et aliberunt ea velenda con-seri onectusdae estissundunt fuga.</p>
</article>
<a class="more" href="#" style="left:330px">mehr</a>

<article class="post" style="left:400px">
  <h2>Sitatur, ipicipi dipsund<br>andit, inis as magna-<br>tentur solorib uscip</h2>
  <p>Laborum quatemp orepell endaepr oviderumtia cus et harum duciendae voloressed uta et, cust, ommostis int aut que ped mil min et, quis ma</p>
</article>
<a class="more" href="#" style="left:547px">mehr</a>

<article class="post" style="left:608px;width:185px">
  <h2>Dolorrovid quatem ra-<br>tem sum, quuntibus,<br>coreriore prem nes</h2>
  <p>Ullestibus is ut quam repelit vidusto volupiet modignatem. Eveligenem quis conseque vit prat occuptam, apicim laut hillam exereru ptibeaqua-tio coris dolupti to maxime ruptae</p>
</article>
<a class="more" href="#" style="left:757px">mehr</a>

<div class="dots" style="top:840px"></div>

<h2 class="section-head" style="left:22px;top:864px">Newsletter</h2>
<p class="small" style="left:50px;top:889px;width:190px">Bestellen Sie meinen Newsletter und werden Sie regelmäßig über jeden neuen Fonds der Top Emittenten informiert.</p>
<div class="field-label" style="left:50px;top:941px;width:81px">Name</div>
<div class="field" style="left:50px;top:963px;width:189px">Name ...</div>
<div class="field-label" style="left:50px;top:987px;width:81px">E-Mail</div>
<div class="field" style="left:50px;top:1010px;width:189px">E-Mail ...</div>
<div class="btn" style="left:156px;top:1034px;width:82px">senden</div>

<div class="vline" style="left:262px"></div>

<h2 class="section-head" style="left:303px;top:864px">Kontakt</h2>
<p class="small" style="left:324px;top:889px;width:190px">Nehem Sie mit uns Kontakt auf und werden Sie regelmäßig über jeden neuen Fonds der Top Emittenten informiert.</p>
<div class="contact">
  <p>Dr. Markus Albrecht</p>
  <p>Fenwick AG<br>Ahornweg 12<br>80469 München</p>
  <p>T: 089 5550140<br>F: 089 5550141</p>
  <p>M.Albrecht@lindenhof-wissensportal.de<br>www.lindenhof-wissensportal.de</p>
</div>

<div class="vline" style="left:532px"></div>

<h2 class="section-head" style="left:575px;top:864px">Suchen</h2>
<p class="small" style="left:597px;top:889px;width:190px">Nehem Sie mit uns Kontakt auf und werden Sie regelmäßig über jeden neuen Fonds der Top Emittenten informiert.</p>
<div class="field" style="left:593px;top:946px;width:188px">suchen ...</div>
<div class="btn" style="left:700px;top:971px;width:81px">suchen</div>

<div class="dots" style="top:1079px"></div>

<p class="legal">Impressum &nbsp;|&nbsp; AGB &nbsp;|&nbsp; Datenschutz &nbsp;|&nbsp; Kontakt</p>

<footer class="site-footer abs">
  Dr. Markus Albrecht &nbsp;|&nbsp; Fenwick AG &nbsp;|&nbsp; Ahornweg 12 &nbsp;|&nbsp; 80469 München<br>
  Tel: 089 5550140 &nbsp;|&nbsp; Fax: 089 5550141 &nbsp;|&nbsp; Mail: M.Albrecht@lindenhof-wissensportal.de &nbsp;|&nbsp; www.lindenhof-wissensportal.de
</footer>

</body>
</html>
```